Quartz Pivot Business Card Design

I need a 2-sided business card for my computer engineering consulting company. The card is expected to convey a message of cutting edge forward thinking, and boldnes. I would like the card to be memorable and stand-out on a desk. The card should be bold, modern, clean, and highly professional. I am a big fan of watermarks/shadows and other intersting but restrained uses of the logo. The card can be a shape other than the traditional rectangle. Perhaps a rectangle with rounded edges. All I ask is the card be able to fit into a standard wallet. I will supply two logos, one with a red background, and one with a black background. Please feel free to work with both of these logos.
Updates

Hi all, thank you for your submissions. I will post the original vector file later today. Thank you for your patience.

Regards,

Martin

Target Market(s)

Engineering Buyers, Vice Presidents and Directors

Industry/Entity Type

Computer

Requirements
Must have
• 2 sides

```html
<!DOCTYPE html>
<html lang="en">
<head>
<meta charset="utf-8">
<title>Quartz Pivot – Business Card</title>
<link rel="stylesheet" href="https://fonts.googleapis.com/css2?family=Questrial&display=swap">
<style>
  :root {
    --page-bg: #d9dde0;
    --card-white: #ffffff;
    --brand-red: #c4282b;
    --brand-red-dark: #8f1c1e;
    --charcoal: #333333;
    --ink: #2b2b2b;
    --watermark: #f6e6e6;
    --tag-grey: #e4e4e4;
    --shadow: rgba(0, 0, 0, 0.18);
  }
  * { box-sizing: border-box; margin: 0; padding: 0; }
  html, body {
    width: 1200px; height: 960px; overflow: hidden;
    background: var(--page-bg);
    font-family: "Questrial", "Century Gothic", sans-serif;
  }
  .sheet {
    width: 1200px; height: 960px;
    display: flex; flex-direction: column; align-items: center; justify-content: center;
    gap: 60px;
  }
  .card {
    position: relative;
    width: 700px; height: 400px;
    border-radius: 18px;
    overflow: hidden;
    box-shadow: 0 10px 30px var(--shadow);
  }

  /* Front */
  .card-front { background: var(--card-white); }
  .card-front .backdrop-circle {
    position: absolute; left: -40px; top: 10px;
    width: 380px; height: 380px; border-radius: 50%;
    background: var(--watermark);
  }
  .name-band {
    position: absolute; left: 330px; right: 0; top: 78px; height: 96px;
    background: var(--charcoal);
    color: var(--card-white);
    padding: 14px 0 0 26px;
  }
  .name-band .person { font-size: 38px; line-height: 1.1; }
  .name-band .role { font-size: 24px; margin-top: 4px; }
  .contact-list {
    position: absolute; left: 340px; top: 232px;
    list-style: none; color: var(--ink);
    font-size: 21px; line-height: 27px;
  }
  .contact-list li { display: flex; align-items: flex-start; gap: 10px; }
  .contact-list .key {
    flex: none; width: 18px; height: 18px; margin-top: 4px;
    background: var(--brand-red); color: var(--card-white);
    border-radius: 3px; font-size: 13px; line-height: 17px; text-align: center;
  }
  .contact-list .indent { padding-left: 28px; }

  /* Back */
  .card-back { background: var(--brand-red); }
  .brand-lockup {
    position: absolute; left: 0; right: 0; top: 70px;
    display: flex; flex-direction: column; align-items: center;
  }
  .brand-square {
    width: 120px; height: 120px; background: var(--charcoal);
    margin-bottom: 22px;
  }
  .brand-name {
    font-size: 46px; color: var(--card-white);
    letter-spacing: 1px; line-height: 1;
  }
  .brand-tagline {
    font-size: 22px; color: var(--tag-grey);
    letter-spacing: 5px; margin-top: 10px;
  }
  .back-rule {
    position: absolute; left: 0; right: 0; bottom: 46px; height: 3px;
    background: var(--brand-red-dark);
  }
</style>
</head>
<body>
<main class="sheet">
  <section class="card card-front" aria-label="Card front">
    <div class="backdrop-circle"></div>
    <div class="name-band">
      <p class="person">Sam Hollis</p>
      <p class="role">IT Director</p>
    </div>
    <ul class="contact-list">
      <li><span class="key">t</span>0123 456 7890 ext 2040</li>
      <li><span class="key">e</span>sam.hollis@quartzpivot.com</li>
      <li><span class="key">w</span>www.quartzpivot.com</li>
      <li><span class="key">a</span>Unit 4, Mill Lane, Easton,</li>
      <li class="indent">EA2 7PL</li>
    </ul>
  </section>

  <section class="card card-back" aria-label="Card back">
    <div class="brand-lockup">
      <div class="brand-square"></div>
      <p class="brand-name">QUARTZ PIVOT</p>
      <p class="brand-tagline">PRECISION AT EVERY TURN</p>
    </div>
    <div class="back-rule"></div>
  </section>
</main>
</body>
</html>
```